依頼詳細
保育園外に設置するチラシ、また近隣に配布するチラシの作成を依頼します。
通りすがりの方が手に取りたくなるような、またチラシの中を見てみたくなる様な
チラシのデザインをお願いしたいです。
記載項目
社名・各園名・住所・TEL番号等
※詳細は、添付ファイルをご確認ください。
サイズ
A4
ページ数
4ページ
希望イメージ
シンプル 複雑
単色 カラフル
暗い 明るい
日常 高級
遊び心 厳粛
未来的 伝統的
女性的 男性的
希望する色
赤系、黄・オレンジ系、水色系
納品ファイル
設定なし
補足説明
パワーポイントでの納品を希望します。
パワーポイント内の保育園の1日は時計表示をしようとして、表記が間違っております。
園の一日の例としては、ホームページを参考にお願いします。
https://hinata-mori.co.jp/programs/day
以上、よろしくお願いいたします。

こちらの求めるデザインに一番合致しており、こちらの期待を上回る提案でした。
パッと見たときの印象、中身のレイアウトなどが優れておりました。

この度は短い期間にもかかわらず、多くの提案をいただき、ありがとうございます。
それぞれの個性があり、選考にはこちらも悩みました。
また同じような機会があれば、ご提案をよろしくお願いいたします。

```html
<!DOCTYPE html>
<html lang="ja">
<head>
<meta charset="UTF-8">
<title>ひなたもり保育園 園見学のお知らせ</title>
<link rel="stylesheet" href="https://fonts.googleapis.com/css2?family=M+PLUS+Rounded+1c:wght@500;700;800&display=swap">
<style>
  :root {
    --bg: #eef6d8;
    --ring-outer: #f6e7a6;
    --ring-line: #f2b58c;
    --disc: #fbeef0;
    --accent: #e5742f;
    --pink: #e9547a;
    --bubble: #f4a0b4;
    --ink: #4a3b34;
    --orange-ink: #e0762b;
    --panel: #ffffff;
    --rule: #f2b58c;
    --trees: #a6d7c6;
    --person: #f5c9a6;
  }
  * { margin: 0; padding: 0; box-sizing: border-box; }
  html, body { width: 829px; height: 1200px; overflow: hidden; }
  body {
    background: var(--bg);
    font-family: "M PLUS Rounded 1c", sans-serif;
    color: var(--ink);
    position: relative;
  }
  .hero { position: absolute; left: 0; top: 0; width: 829px; height: 660px; }
  .hero-svg { position: absolute; left: 0; top: 0; }
  .brand-card {
    position: absolute;
    left: 228px; width: 378px;
    background: #fff;
    border-radius: 16px;
    display: flex; flex-direction: column; align-items: center; justify-content: center;
    font-weight: 700;
    color: var(--accent);
    white-space: nowrap;
  }
  .brand-card--school { top: 222px; height: 82px; flex-direction: row; gap: 10px; font-size: 21px; }
  .brand-card--nursery { top: 322px; height: 100px; font-size: 32px; line-height: 1.2; }
  .brand-tagline { font-size: 14px; font-weight: 500; color: var(--accent); margin-top: 4px; }
  .brand-dot { width: 20px; height: 20px; border-radius: 50%; background: var(--bubble); flex: none; }
  .intro {
    position: absolute; top: 446px; left: 0; width: 829px;
    text-align: center; font-size: 44px; font-weight: 800; color: var(--pink);
  }
  .notice {
    position: absolute; left: 33px; top: 705px; width: 767px; height: 455px;
    background: var(--panel); border-radius: 28px; overflow: hidden;
  }
  .notice-title {
    position: absolute; left: 90px; top: 24px;
    font-size: 28px; font-weight: 700; color: var(--ink); white-space: nowrap;
  }
  .notice-rule {
    position: absolute; left: 80px; top: 72px; width: 460px; height: 3px;
    background: var(--rule);
  }
  .trees {
    position: absolute; right: 24px; top: 14px; width: 180px; height: 66px;
    border-radius: 12px;
    background: linear-gradient(90deg, #f6b7a8, var(--trees), #f5d77e);
    opacity: .8;
  }
  .person {
    position: absolute; left: 10px; bottom: 0; width: 190px; height: 230px;
    border-radius: 60px 60px 0 0;
    background: linear-gradient(180deg, var(--person), #f3a64c);
    opacity: .85;
  }
  .bubble {
    position: absolute; left: 20px; top: 92px; width: 150px; height: 150px;
    border-radius: 50%; background: var(--bubble);
    display: flex; align-items: center; justify-content: center;
    text-align: center; color: #fff; font-weight: 700; font-size: 19px; line-height: 1.45;
    white-space: nowrap; z-index: 1;
  }
  .details { position: absolute; left: 240px; top: 100px; }
  .row { display: flex; align-items: center; color: var(--orange-ink); font-weight: 700; font-size: 18px; white-space: nowrap; }
  .row dt { width: 96px; letter-spacing: 4px; }
  .row dd { color: var(--ink); }
  .row--date { height: 66px; }
  .row--date .day { font-size: 50px; font-weight: 800; margin: 0 8px; color: var(--ink); }
  .row--time { height: 50px; }
  .row--place { margin-top: 22px; height: 30px; }
  .row--address { height: 30px; }
  .phone {
    position: absolute; left: 248px; top: 338px;
    display: flex; align-items: center; gap: 18px;
    font-size: 44px; font-weight: 800; color: var(--pink); letter-spacing: 1px; white-space: nowrap;
  }
</style>
</head>
<body>
  <section class="hero">
    <svg class="hero-svg" width="829" height="660" viewBox="0 0 829 660">
      <defs>
        <path id="arc-top" d="M 150 326 A 265 265 0 0 1 680 326"/>
        <path id="arc-bottom" d="M 115 326 A 300 300 0 0 0 715 326"/>
      </defs>
      <circle cx="415" cy="326" r="310" fill="var(--ring-outer)" stroke="var(--ring-line)" stroke-width="6"/>
      <circle cx="415" cy="326" r="236" fill="var(--disc)" stroke="var(--ring-line)" stroke-width="6"/>
      <text font-size="34" font-weight="800" fill="var(--orange-ink)" font-family="M PLUS Rounded 1c, sans-serif">
        <textPath href="#arc-top" startOffset="50%" text-anchor="middle">ひなたもり保育園は</textPath>
      </text>
      <text font-size="34" font-weight="800" fill="var(--orange-ink)" font-family="M PLUS Rounded 1c, sans-serif" dy="-12">
        <textPath href="#arc-bottom" startOffset="50%" text-anchor="middle">3歳からの入園がとってもお得なんです！</textPath>
      </text>
    </svg>
    <div class="brand-card brand-card--school"><span class="brand-dot"></span>ひなたもりナーサリースクール</div>
    <div class="brand-card brand-card--nursery">ひなたもり保育園<span class="brand-tagline">子どもたちが夢と希望をもてるように</span></div>
    <p class="intro">のご紹介</p>
  </section>

  <section class="notice">
    <h2 class="notice-title">1月度 園見学のお知らせ</h2>
    <div class="notice-rule"></div>
    <div class="trees" role="img" aria-label="色とりどりの木のイラスト"></div>
    <div class="person" role="img" aria-label="電話をかける女性のイラスト"></div>
    <div class="bubble">お気軽に<br>お申込み下さい</div>

    <dl class="details">
      <div class="row row--date"><dt>日 時：</dt><dd>2023年<span class="day">1/11</span>（水）</dd></div>
      <div class="row row--time"><dt>時 間：</dt><dd>午前10:30〜</dd></div>
      <div class="row row--place"><dt>場 所：</dt><dd>ひなたもりナーサリースクールみどり</dd></div>
      <div class="row row--address"><dt>住 所：</dt><dd>東京都足立区緑町2-8-11</dd></div>
    </dl>

    <div class="phone">
      <svg width="34" height="46" viewBox="0 0 34 46" aria-hidden="true">
        <rect x="3" y="3" width="28" height="40" rx="5" fill="none" stroke="var(--ink)" stroke-width="4"/>
        <line x1="12" y1="36" x2="22" y2="36" stroke="var(--ink)" stroke-width="3"/>
      </svg>
      <span>03-5550-0142</span>
    </div>
  </section>
</body>
</html>
```